resleeving

we need a revamped flyer to email to our existing customers

ensure all spelling is correct

if using sentences make sure to use centre margins

```html
<!DOCTYPE html>
<html lang="en">
<head>
<meta charset="utf-8">
<title>Summit Auto Works – Stainless Steel Resleeving</title>
<link rel="stylesheet" href="https://fonts.googleapis.com/css2?family=Arimo:wght@400;700&display=swap">
<style>
  :root {
    --yellow: #e6e60a;
    --gold: #e3b900;
    --black: #050505;
    --ink: #111111;
    --white: #ececec;
    --page: #ececec;
    --thumb: #cfcfcf;
  }
  * { margin: 0; padding: 0; box-sizing: border-box; }
  html, body { width: 1200px; height: 1200px; overflow: hidden; background: var(--page); }
  body { font-family: "Arimo", Arial, sans-serif; }

  .flyer { position: absolute; left: 180px; top: 0; width: 840px; height: 1200px; background: var(--black); overflow: hidden; }
  .flyer-shapes { position: absolute; inset: 0; }

  .hero-photo { position: absolute; left: 398px; top: 0; width: 442px; height: 501px;
    background: linear-gradient(135deg, #c9ccd0 0%, #9aa2ab 45%, #4b5a70 100%); }

  .brand { position: absolute; left: 0; top: 0; width: 340px; height: 236px; display: flex; flex-direction: column; align-items: center; justify-content: center; gap: 18px; }
  .brand-square { width: 64px; height: 64px; background: var(--ink); }
  .brand-name { font-weight: 700; font-size: 22px; color: var(--ink); letter-spacing: .3px; }

  .headline { position: absolute; left: 84px; top: 268px; font-weight: 700; font-size: 74px; line-height: 67px; color: var(--white); letter-spacing: -.5px; }
  .headline .accent { color: var(--gold); }
  .headline-bar { position: absolute; left: 51px; top: 278px; width: 5px; height: 183px; background: var(--gold); }

  .tagline { position: absolute; left: 0; top: 509px; width: 840px; height: 56px; background: var(--yellow); display: flex; align-items: center; justify-content: center; font-weight: 700; font-size: 40px; color: var(--ink); letter-spacing: -.3px; }

  .part-row { position: absolute; left: 40px; top: 588px; display: flex; gap: 19px; }
  .part-thumb { width: 138px; height: 96px; border: 4px solid var(--yellow); background: linear-gradient(160deg, #e4e4e4, var(--thumb)); }

  .question { position: absolute; left: 40px; top: 702px; width: 516px; height: 58px; background: var(--yellow); border-radius: 0 29px 29px 0; display: flex; align-items: center; padding-left: 16px; font-weight: 700; font-size: 29px; color: var(--ink); }

  .benefits { position: absolute; left: 40px; top: 777px; list-style: none; }
  .benefits li { display: flex; align-items: center; gap: 6px; height: 34.5px; font-size: 25px; color: var(--white); }
  .benefits svg { width: 24px; height: 24px; flex: none; }

  .aim { position: absolute; left: 40px; top: 966px; font-weight: 700; font-size: 27px; line-height: 29px; color: var(--white); }
  .aim .accent { color: var(--gold); }

  .contact { position: absolute; left: 0; top: 1085px; width: 840px; height: 105px; background: var(--yellow); color: var(--ink); font-size: 19px; }
  .contact-col { position: absolute; top: 14px; line-height: 25px; }
  .contact-col.address { left: 40px; }
  .contact-col.phones { left: 325px; }
  .contact-col.online { left: 528px; top: 39px; }
  .contact-col .name { font-weight: 700; font-size: 21px; }
  .contact-divider { position: absolute; top: 16px; width: 2px; height: 73px; background: var(--ink); }
  .contact-line { display: flex; align-items: center; gap: 6px; }
  .contact-line svg { width: 15px; height: 15px; flex: none; }
</style>
</head>
<body>
<main class="flyer">
  <div class="hero-photo" role="img" aria-label="Photo of a technician's hands fitting a sleeve into a brake cylinder"></div>

  <svg class="flyer-shapes" viewBox="0 0 840 1200" aria-hidden="true">
    <polygon points="0,0 490,0 363,236 0,236" fill="var(--yellow)"/>
    <polygon points="490,0 500,0 373,236 363,236" fill="#f4f4f4"/>
    <polygon points="0,236 363,236 373,236 570,236 650,370 578,501 0,501" fill="var(--black)"/>
    <polygon points="577,236 595,236 673,370 595,501 577,501 655,370" fill="var(--yellow)"/>
    <rect x="0" y="501" width="840" height="8" fill="#f4f4f4"/>
    <rect x="0" y="1190" width="840" height="10" fill="var(--black)"/>
  </svg>

  <header class="brand">
    <div class="brand-square"></div>
    <div class="brand-name">SUMMIT AUTO WORKS</div>
  </header>

  <div class="headline-bar"></div>
  <h1 class="headline">STAINLESS<br><span class="accent">STEEL</span><br>RESLEEVING</h1>

  <p class="tagline">THE BRAKE AND CABLE SPECIALISTS</p>

  <div class="part-row">
    <div class="part-thumb" role="img" aria-label="Photo of a brake booster housing"></div>
    <div class="part-thumb" role="img" aria-label="Photo of a clutch slave cylinder assembly"></div>
    <div class="part-thumb" role="img" aria-label="Photo of a brake servo unit"></div>
    <div class="part-thumb" role="img" aria-label="Photo of a brake master cylinder with reservoir"></div>
    <div class="part-thumb" role="img" aria-label="Photo of a wheel cylinder"></div>
  </div>

  <h2 class="question">Why re-sleeve your cylinders?</h2>

  <ul class="benefits">
    <li><svg viewBox="0 0 24 24"><circle cx="12" cy="12" r="10" fill="none" stroke="var(--yellow)" stroke-width="2"/><path d="M7 12l4 4 8-10" fill="none" stroke="var(--yellow)" stroke-width="2.4" stroke-linecap="round"/></svg>Cost effective</li>
    <li><svg viewBox="0 0 24 24"><circle cx="12" cy="12" r="10" fill="none" stroke="var(--yellow)" stroke-width="2"/><path d="M7 12l4 4 8-10" fill="none" stroke="var(--yellow)" stroke-width="2.4" stroke-linecap="round"/></svg>Longer Lasting</li>
    <li><svg viewBox="0 0 24 24"><circle cx="12" cy="12" r="10" fill="none" stroke="var(--yellow)" stroke-width="2"/><path d="M7 12l4 4 8-10" fill="none" stroke="var(--yellow)" stroke-width="2.4" stroke-linecap="round"/></svg>No waiting for overseas parts</li>
    <li><svg viewBox="0 0 24 24"><circle cx="12" cy="12" r="10" fill="none" stroke="var(--yellow)" stroke-width="2"/><path d="M7 12l4 4 8-10" fill="none" stroke="var(--yellow)" stroke-width="2.4" stroke-linecap="round"/></svg>Re-manufacturing = Re-cycling</li>
    <li><svg viewBox="0 0 24 24"><circle cx="12" cy="12" r="10" fill="none" stroke="var(--yellow)" stroke-width="2"/><path d="M7 12l4 4 8-10" fill="none" stroke="var(--yellow)" stroke-width="2.4" stroke-linecap="round"/></svg>Cylinders are no longer available</li>
  </ul>

  <p class="aim"><span class="accent">Our Aim Is To Have Your Parts Repaired</span><br>With The Quickest<br>Turn-around Times Possible</p>

  <footer class="contact">
    <div class="contact-col address">
      <div class="name">Summit Auto Works</div>
      <div>27 Fernhill Road, Hamilton</div>
      <div>unsubscribe from this list</div>
    </div>
    <div class="contact-divider" style="left:306px"></div>
    <div class="contact-col phones">
      <div class="contact-line"><svg viewBox="0 0 16 16"><path d="M3 1.5l3 .5 1 3-2 1.5a9 9 0 0 0 4.5 4.5L11 9l3 1 .5 3-2 1.5C7 14 2 9 1.5 3.5z" fill="var(--ink)"/></svg>0800 55 41 82</div>
      <div class="contact-line"><svg viewBox="0 0 16 16"><path d="M3 1.5l3 .5 1 3-2 1.5a9 9 0 0 0 4.5 4.5L11 9l3 1 .5 3-2 1.5C7 14 2 9 1.5 3.5z" fill="var(--ink)"/></svg>07 555 0143</div>
      <div class="contact-line"><svg viewBox="0 0 16 16"><rect x="4" y="2" width="8" height="4" fill="none" stroke="var(--ink)" stroke-width="1.5"/><rect x="1.5" y="6" width="13" height="8" rx="1" fill="var(--ink)"/></svg>07 555 0144</div>
    </div>
    <div class="contact-divider" style="left:499px"></div>
    <div class="contact-col online">
      <div class="contact-line"><svg viewBox="0 0 16 16"><rect x="1.5" y="3.5" width="13" height="9" fill="var(--ink)"/><path d="M1.5 3.5l6.5 5 6.5-5" fill="none" stroke="var(--yellow)" stroke-width="1.2"/></svg>parts@summitautoworks.co.nz</div>
      <div class="contact-line"><svg viewBox="0 0 16 16"><circle cx="8" cy="8" r="6.5" fill="none" stroke="var(--ink)" stroke-width="1.6"/><ellipse cx="8" cy="8" rx="2.8" ry="6.5" fill="none" stroke="var(--ink)" stroke-width="1.2"/><path d="M1.5 8h13" stroke="var(--ink)" stroke-width="1.2"/></svg>www.summitautoworks.co.nz</div>
    </div>
  </footer>
</main>
</body>
</html>
```